Business Card Design Project

We require a professional business card designed for our consulting organisation that has the same theme and colours as our logo except for the grey.

Colours on the front should predominately be white however some reference to our logo colours except for the grey.

The back of the card should be have background colour that aligns with our logo colour.

Layout, style and design is up to the designer. So send through your designs

Details are attached in the word document project brief.

Target Market(s)

Target market are large corporate organisations

Industry/Entity Type

Business

Requirements
Must have
• Content on the front must have:

Dean Halvorsen
Managing Director

P: 0417 285 394
E: Dean@brevolinkpartners.com
W: www.brevolinkpartners.com

Content on the back must have the words:
Alliances
Placement
Training
Support

Design Colours
Must align to our logo

```html
<!DOCTYPE html>
<html lang="en">
<head>
<meta charset="utf-8">
<title>Brevolink Partners – Business Card</title>
<link rel="stylesheet" href="https://fonts.googleapis.com/css2?family=Arimo:wght@400;700&display=swap">
<style>
  :root {
    --page-bg: #e9ecef;
    --brand-blue: #1370bf;
    --brand-blue-deep: #1565b5;
    --brand-blue-light: #2196d6;
    --card-white: #ffffff;
    --text-on-blue: #ffffff;
    --card-shadow: 0 10px 28px rgba(0, 0, 0, 0.18);
  }
  * { margin: 0; padding: 0; box-sizing: border-box; }
  html, body {
    width: 1200px;
    height: 900px;
    overflow: hidden;
    background: var(--page-bg);
    font-family: "Arimo", Arial, sans-serif;
  }
  .canvas {
    position: relative;
    width: 1200px;
    height: 900px;
  }
  .card {
    position: absolute;
    width: 620px;
    height: 378px;
    border-radius: 4px;
    box-shadow: var(--card-shadow);
    overflow: hidden;
  }

  /* Back of card */
  .card-back {
    left: 80px;
    top: 70px;
    background: var(--brand-blue);
    color: var(--text-on-blue);
  }
  .back-brand {
    position: absolute;
    left: 70px;
    top: 120px;
    display: flex;
    align-items: center;
    gap: 20px;
  }
  .brand-dot {
    width: 58px;
    height: 58px;
    border-radius: 50%;
    background: var(--text-on-blue);
  }
  .brand-name {
    font-weight: 700;
    font-size: 40px;
    line-height: 1.05;
    letter-spacing: 0.5px;
  }
  .services {
    position: absolute;
    left: 70px;
    top: 232px;
    display: flex;
    gap: 12px;
    font-weight: 700;
    font-size: 19px;
    letter-spacing: 0.3px;
  }
  .services .sep { opacity: 0.9; }

  /* Front of card */
  .card-front {
    left: 500px;
    top: 452px;
    background: var(--card-white);
  }
  .front-decoration {
    position: absolute;
    left: 0;
    top: 0;
    width: 300px;
    height: 100%;
    background: linear-gradient(135deg, var(--brand-blue-deep) 0%, var(--brand-blue-light) 100%);
  }
  .contact {
    position: absolute;
    right: 44px;
    bottom: 50px;
    text-align: right;
    color: var(--brand-blue-deep);
  }
  .contact-name {
    font-weight: 700;
    font-size: 22px;
  }
  .contact-role {
    font-size: 14px;
    color: var(--brand-blue-light);
    margin-top: 2px;
  }
  .contact-lines {
    margin-top: 30px;
    font-size: 15px;
    line-height: 1.45;
  }
  .contact-lines .label { font-weight: 700; color: var(--brand-blue-deep); }
  .contact-lines .value { color: var(--brand-blue-light); }
  .contact-web {
    font-weight: 700;
    font-size: 16px;
  }
</style>
</head>
<body>
<main class="canvas">

  <section class="card card-back" aria-label="Business card back">
    <div class="back-brand">
      <span class="brand-dot" aria-hidden="true"></span>
      <div class="brand-name">Brevolink<br>Partners</div>
    </div>
    <p class="services">
      <span>Alliances</span><span class="sep">•</span>
      <span>Placement</span><span class="sep">•</span>
      <span>Training</span><span class="sep">•</span>
      <span>Support</span>
    </p>
  </section>

  <section class="card card-front" aria-label="Business card front">
    <div class="front-decoration" role="img" aria-label="Large brand decoration in blue tones"></div>
    <div class="contact">
      <p class="contact-name">Dean Halvorsen</p>
      <p class="contact-role">Managing Director</p>
      <div class="contact-lines">
        <p><span class="label">P:</span> <span class="value">0417 285 394</span></p>
        <p><span class="label">E:</span> <span class="value">Dean@brevolinkpartners.com</span></p>
        <p class="contact-web">www.brevolinkpartners.com</p>
      </div>
    </div>
  </section>

</main>
</body>
</html>
```